Business Card Design

We are a manufacturing company that has been in business for over 30 years, established in 1981. We are looking to increase our business with defence force, government, and the major telecoms so the card needs to present the company as being cutting edge, secure, and professional.
Industry/Entity Type
Defence
Contact Information for Business Card
Name Gareth Olsund
Phone 02 9374 6815
Fax 02 9457 3162
mobile 0438260517
Email Gary@Korvex.com.au
Webiste www.korvex.com.au
ABN 58 006 391 842
address: 17 Belcor Street Ingleburn NSW 2565
"Manufacturer of Antennas, GPS, Microwave, Cable Assemblies, RF, Military, & Telecommunications"
Look and feel

```html
<!DOCTYPE html>
<html lang="en">
<head>
<meta charset="utf-8">
<title>Korvex Business Card</title>
<link rel="stylesheet" href="https://fonts.googleapis.com/css2?family=Arimo:wght@400;700&family=Roboto+Condensed:wght@700&display=swap">
<style>
  :root {
    --stage: #2b2b2b;
    --navy: #1f2a6b;
    --orange: #e0522a;
    --ink: #111111;
    --card-white: #ffffff;
    --card-grey-light: #ececec;
    --card-grey-dark: #9a9a9a;
  }
  * { box-sizing: border-box; margin: 0; padding: 0; }
  html, body {
    width: 1200px; height: 900px; overflow: hidden;
    background: var(--stage);
    font-family: "Arimo", Arial, sans-serif;
  }
  .stage {
    width: 1200px; height: 900px;
    display: flex; align-items: center; justify-content: center; gap: 40px;
  }
  .card {
    position: relative; width: 540px; height: 330px; overflow: hidden;
    box-shadow: 0 10px 30px rgba(0,0,0,0.5);
  }

  /* Brand lockup: square above name */
  .brand { position: absolute; display: flex; flex-direction: column; align-items: center; gap: 6px; }
  .brand-square { width: 90px; height: 74px; background: var(--navy); }
  .brand-name {
    font-family: "Roboto Condensed", "Arial Narrow", sans-serif;
    font-weight: 700; font-size: 18px; letter-spacing: 3px; color: var(--orange);
  }
  .faint-mark { position: absolute; border-radius: 50%; }

  /* Back */
  .card-back {
    background: linear-gradient(135deg, var(--card-grey-light) 0%, #cfcfcf 50%, var(--card-grey-dark) 100%);
  }
  .card-back .brand { top: 34px; right: 60px; }
  .card-back .website {
    position: absolute; top: 150px; right: 40px;
    font-size: 16px; color: var(--navy);
  }
  .card-back .tagline {
    position: absolute; top: 178px; right: 40px; width: 330px; text-align: right;
    font-family: "Roboto Condensed", "Arial Narrow", sans-serif;
    font-size: 16px; font-weight: 700; line-height: 1.35; color: var(--orange);
  }
  .card-back .faint-mark {
    left: 10px; bottom: -40px; width: 300px; height: 240px;
    background: radial-gradient(circle, rgba(110,110,110,0.28) 0%, rgba(110,110,110,0) 70%);
  }

  /* Front */
  .card-front { background: var(--card-white); }
  .card-front .faint-mark {
    right: 10px; top: 10px; width: 280px; height: 240px;
    background: radial-gradient(circle, rgba(224,82,42,0.10) 0%, rgba(190,190,190,0.14) 45%, rgba(255,255,255,0) 70%);
  }
  .card-front .brand { top: 24px; left: 46px; }
  .holder-tab {
    position: absolute; left: 0; top: 160px; width: 22px; height: 40px;
    background: var(--navy); border-radius: 0 10px 10px 0;
  }
  .holder-name {
    position: absolute; left: 32px; top: 156px;
    font-size: 34px; font-weight: 400; color: var(--navy);
  }
  .holder-name .surname { color: var(--orange); }
  .contact {
    position: absolute; left: 32px; top: 208px;
    display: flex; flex-direction: column; gap: 6px;
    font-family: "Roboto Condensed", "Arial Narrow", sans-serif;
    font-size: 19px; font-weight: 700; color: var(--ink);
  }
  .contact-row { display: flex; align-items: center; gap: 12px; white-space: nowrap; }
  .contact-item { display: flex; align-items: center; gap: 6px; }
  .icon { width: 16px; height: 16px; fill: var(--ink); flex: none; }
</style>
</head>
<body>
<main class="stage">

  <section class="card card-back" aria-label="Card back">
    <div class="faint-mark" role="img" aria-label="Faint enlarged brand mark"></div>
    <div class="brand">
      <span class="brand-square"></span>
      <span class="brand-name">KORVEX</span>
    </div>
    <p class="website">www.korvex.com.au</p>
    <p class="tagline">Manufacturer of Antennas, GPS, Microwave, Cable Assemblies, RF, Military, &amp; Telecommunications</p>
  </section>

  <section class="card card-front" aria-label="Card front">
    <div class="faint-mark" role="img" aria-label="Faint enlarged brand mark"></div>
    <div class="brand">
      <span class="brand-square"></span>
      <span class="brand-name">KORVEX</span>
    </div>
    <span class="holder-tab"></span>
    <h1 class="holder-name">Gareth <span class="surname">Olsund</span></h1>

    <div class="contact">
      <div class="contact-row">
        <span class="contact-item">17 Belcor Street Tallowbrook NSW 2598</span>
        <span class="contact-item">
          <svg class="icon" viewBox="0 0 16 16"><rect x="4" y="1" width="8" height="5"/><rect x="1" y="6" width="14" height="7" rx="1"/><rect x="4" y="11" width="8" height="4"/></svg>
          02 9457 3162
        </span>
      </div>
      <div class="contact-row">
        <span class="contact-item">
          <svg class="icon" viewBox="0 0 16 16"><rect x="4" y="1" width="8" height="14"/><rect x="2" y="14" width="12" height="2"/></svg>
          02 9374 6815
        </span>
        <span class="contact-item">
          <svg class="icon" viewBox="0 0 16 16"><path d="M3 1h4l1 4-2 1.5a9 9 0 0 0 3.5 3.5L11 8l4 1v4a2 2 0 0 1-2 2C6.5 15 1 9.5 1 3a2 2 0 0 1 2-2z"/></svg>
          0438260517
        </span>
      </div>
      <div class="contact-row">
        <span class="contact-item">
          <svg class="icon" viewBox="0 0 16 16"><path d="M4 0h8a1 1 0 0 1 1 1v14a1 1 0 0 1-1 1H4a1 1 0 0 1-1-1V1a1 1 0 0 1 1-1zm1 2v10h6V2z"/></svg>
          Gary@Korvex.com.au
        </span>
        <span class="contact-item">
          <svg class="icon" viewBox="0 0 16 16"><circle cx="8" cy="8" r="6.5" fill="none" stroke="#111" stroke-width="1.3"/><ellipse cx="8" cy="8" rx="2.8" ry="6.5" fill="none" stroke="#111" stroke-width="1.1"/><line x1="1.5" y1="8" x2="14.5" y2="8" stroke="#111" stroke-width="1.1"/></svg>
          www.korvex.com.au
        </span>
      </div>
      <div class="contact-row">ABN 58 006 391 842</div>
    </div>
  </section>

</main>
</body>
</html>
```